Financial Planning business needs a new Business Card design

We need a business card design for an Australian financial planning business. I am looking for a clean simple design

Target Market(s)

People aged 25-40

Industry/Entity Type

Financial Service

Contact Information for Business Card

On the front of the card we need the following information:
Name: Colin Merrow (First Name Green: #006838 and last name Grey: #414042)
Position: Financial Adviser
Qualifications: BEc(Hons), AdDipFS(FP), Dip FMBM, CFL®
Mobile: 0437 512 604
Email: colin@brightledgeplan.com.au

On the back of the card we need:
Postal address: PO BOX 5307, PERTH BC, WA 6849
Website: www.brightledgeplan.com.au
Text: AFS Licence No. 518760

The fields need to be able to be edited.

Font styles to use
Sans Serif

Requirements
Must have
• Information listed above

```html
<!DOCTYPE html>
<html lang="en">
<head>
<meta charset="utf-8">
<title>Brightledge Business Card</title>
<link rel="stylesheet" href="https://fonts.googleapis.com/css2?family=Roboto:wght@300;400;700&display=swap">
<style>
  :root {
    --green: #006838;
    --green-deep: #004d29;
    --grey-text: #414042;
    --grey-soft: #6d6e71;
    --stripe: #eeeeee;
    --card: #ffffff;
    --backdrop: #e4e5e7;
  }
  * { margin: 0; padding: 0; box-sizing: border-box; }
  html, body { width: 1200px; height: 800px; overflow: hidden; }
  body {
    background: var(--backdrop);
    font-family: "Roboto", Helvetica, Arial, sans-serif;
    color: var(--grey-text);
    position: relative;
  }
  .card {
    position: absolute;
    top: 235px;
    width: 540px;
    height: 330px;
    background: var(--card);
    overflow: hidden;
    box-shadow: 0 10px 30px rgba(0,0,0,0.18);
  }
  .card-back { left: 40px; }
  .card-front { left: 620px; }
  .card svg.art { position: absolute; inset: 0; width: 100%; height: 100%; }

  /* Back */
  .brand {
    position: absolute;
    left: 128px; top: 142px;
    display: flex; align-items: center; gap: 10px;
  }
  .brand-mark { width: 18px; height: 18px; background: var(--green); }
  .brand-name {
    font-weight: 700; font-size: 40px; letter-spacing: 1px;
    color: var(--green); line-height: 1;
  }
  .licence {
    position: absolute; right: 28px; top: 98px;
    font-size: 14px; font-weight: 400; color: var(--grey-text);
  }
  .back-web {
    position: absolute; left: 130px; top: 214px;
    font-size: 13px; color: var(--grey-text);
  }
  .back-postal {
    position: absolute; left: 130px; top: 234px;
    font-size: 11px; color: var(--grey-soft); letter-spacing: .3px;
  }

  /* Front */
  .identity { position: absolute; left: 76px; top: 72px; width: 222px; }
  .name { font-size: 25px; font-weight: 300; line-height: 1.1; letter-spacing: .3px; white-space: nowrap; }
  .name .first { color: var(--green); }
  .name .last { color: var(--grey-text); font-weight: 400; }
  .role { font-size: 13px; font-weight: 300; margin-top: 6px; color: var(--grey-text); }
  .quals { font-size: 8px; font-weight: 300; margin-top: 4px; color: var(--grey-soft); white-space: nowrap; }

  .contacts { position: absolute; left: 316px; top: 84px; list-style: none; }
  .contacts li {
    display: flex; align-items: center; gap: 12px;
    min-height: 36px; font-size: 11.5px; font-weight: 300; line-height: 1.3; color: var(--grey-text);
  }
  .contacts .icon {
    width: 26px; height: 26px; border-radius: 50%;
    background: var(--card); box-shadow: 0 0 0 1px #dcdcdc;
    display: flex; align-items: center; justify-content: center; flex: none;
  }
  .contacts .icon svg { width: 14px; height: 14px; }
</style>
</head>
<body>

<section class="card card-back" aria-label="Business card back">
  <svg class="art" viewBox="0 0 540 330" aria-hidden="true">
    <polygon points="0,250 540,60 540,110 0,300" fill="var(--stripe)"/>
    <polygon points="0,0 300,0 0,150" fill="var(--green-deep)"/>
    <polygon points="0,150 300,0 420,0 0,200" fill="var(--green)"/>
    <polygon points="360,330 460,240 540,330" fill="var(--green)"/>
    <polygon points="410,330 460,282 500,330" fill="var(--card)"/>
  </svg>
  <div class="brand">
    <span class="brand-mark"></span>
    <span class="brand-name">BRIGHTLEDGE</span>
  </div>
  <p class="licence">AFS Licence No. 518760</p>
  <p class="back-web">www.brightledgeplan.com.au</p>
  <p class="back-postal">PO BOX 5307, PERTH BC, WA 6849</p>
</section>

<section class="card card-front" aria-label="Business card front">
  <svg class="art" viewBox="0 0 540 330" aria-hidden="true">
    <polygon points="0,270 540,120 540,170 0,320" fill="var(--stripe)"/>
    <polygon points="30,0 330,0 346,250 40,282" fill="var(--green)"/>
    <rect x="58" y="18" width="258" height="222" rx="10" fill="var(--card)"/>
  </svg>

  <div class="identity">
    <h1 class="name"><span class="first">COLIN</span> <span class="last">MERROW</span></h1>
    <p class="role">Financial Adviser</p>
    <p class="quals">BEc(Hons), AdDipFS(FP), Dip FMBM, CFL®</p>
  </div>

  <ul class="contacts">
    <li><span class="icon"><svg viewBox="0 0 16 16"><rect x="1" y="3" width="14" height="10" fill="var(--grey-text)"/><polyline points="1,3 8,9 15,3" fill="none" stroke="#fff" stroke-width="1.4"/></svg></span>colin@brightledgeplan.com.au</li>
    <li><span class="icon"><svg viewBox="0 0 16 16"><path d="M4 1 L7 4 L5 6 Q7 10 10 11 L12 9 L15 12 L12 15 Q3 13 1 4 Z" fill="var(--grey-text)"/></svg></span>0437 512 604</li>
    <li><span class="icon"><svg viewBox="0 0 16 16"><polygon points="8,1 15,8 13,8 13,15 3,15 3,8 1,8" fill="var(--grey-text)"/></svg></span><span>PO BOX 5307,<br>PERTH BC, WA 6849</span></li>
    <li><span class="icon"><svg viewBox="0 0 16 16"><circle cx="8" cy="8" r="7" fill="var(--grey-text)"/><ellipse cx="8" cy="8" rx="3" ry="7" fill="none" stroke="#fff" stroke-width="1"/><line x1="1" y1="8" x2="15" y2="8" stroke="#fff" stroke-width="1"/></svg></span>www.brightledgeplan.com.au</li>
  </ul>
</section>

</body>
</html>
```